Business Card Design Project

Basketball Training program

Offers: Travel Club Program - Camps - Clinics - Private Training

website: rivetbasketball.example
Phone Contact: Main Phone: 555-317-4826
Email: rivet.basketball@mailbox.example

Industry/Entity Type

Business

Contact Information for Business Card

Need one for the following coaches:
Marlo Quintrell - Boys & Girls Basketball Coach
Noweni Tasker - Girls Basketball Coach
Anselmo Duvray - Director/Head Coach
Hollis Ruk- Boys Basketball
Warren Olivash - Boys Basketball
Tomas Ferlanga - Boys Basketball
Kavin Sotherby- Boys Basketball/ Trainer
Al Varnock - Boys & Girls Basketball Coach

Basketball Training program Logo - one side

Logo on the corner
new one on the left (RB)
old one on the right (old one is with the rivet and basketball)

```html
<!DOCTYPE html>
<html lang="en">
<head>
<meta charset="utf-8">
<title>Rivet Basketball – Business Card</title>
<link rel="stylesheet" href="https://fonts.googleapis.com/css2?family=Baloo+2:wght@700&family=Libre+Baskerville:wght@400;700&display=swap">
<style>
  :root {
    --page: #8a8a8a;
    --card: #0d0d0d;
    --card-edge: #1a1a1a;
    --gold: #f2b01e;
    --gold-light: #fcd97a;
    --gold-text: #f7d36a;
    --glow: rgba(242, 176, 30, 0.55);
    --faint: rgba(255, 255, 255, 0.05);
  }
  * { box-sizing: border-box; margin: 0; padding: 0; }
  html, body {
    width: 1200px; height: 520px; overflow: hidden;
    background: var(--page);
  }
  .canvas { position: relative; width: 1200px; height: 520px; }

  .card {
    position: absolute; top: 110px;
    width: 500px; height: 300px;
    background: radial-gradient(ellipse at 55% 45%, var(--card-edge), var(--card) 70%);
    overflow: hidden;
  }
  .card--front { left: 70px; }
  .card--back { left: 640px; }

  .net-decoration {
    position: absolute; left: 160px; top: 30px;
    width: 200px; height: 250px;
    background: radial-gradient(ellipse at center, var(--faint), transparent 70%);
  }
  .card--back .net-decoration { left: 170px; top: 20px; }

  /* Front */
  .program-title {
    position: absolute; top: 44px; left: 0; width: 100%;
    text-align: center;
    font-family: "Baloo 2", sans-serif; font-weight: 700;
    font-size: 23px; letter-spacing: 0.5px;
    color: var(--gold-light);
    text-shadow: 0 0 6px var(--glow), 1px 1px 0 #000;
  }
  .offer {
    position: absolute;
    display: flex; flex-direction: column; align-items: center; gap: 4px;
  }
  .offer svg { display: block; overflow: visible; }
  .offer svg * { stroke: var(--gold); fill: none; stroke-width: 2.2; stroke-linejoin: round; filter: drop-shadow(0 0 2px var(--glow)); }
  .offer-label {
    font-family: "Libre Baskerville", serif; font-weight: 700;
    color: var(--gold);
    text-shadow: 0 0 4px var(--glow), 1px 1px 0 #000;
    white-space: nowrap; line-height: 1.2;
  }
  .offer--travel { left: 84px; top: 88px; width: 160px; }
  .offer--travel .offer-label { font-size: 13px; }
  .offer--camps { left: 330px; top: 100px; width: 90px; }
  .offer--camps .offer-label { font-size: 17px; }
  .offer--clinics { left: 86px; top: 178px; width: 100px; }
  .offer--clinics .offer-label { font-size: 17px; }
  .offer--private { left: 296px; top: 176px; width: 150px; }
  .offer--private .offer-label { font-size: 13px; }
  .player-figure {
    display: block; align-self: flex-end; margin-right: 6px;
    width: 42px; height: 56px; border-radius: 18px 18px 6px 6px;
    background: linear-gradient(180deg, rgba(242,176,30,0.35), rgba(242,176,30,0.12));
  }

  /* Back */
  .mark-rb {
    position: absolute; left: 44px; top: 40px;
    width: 78px; height: 78px; border-radius: 50%;
    border: 3px solid #000;
    box-shadow: 0 0 10px var(--glow);
    display: flex; align-items: center; justify-content: center;
    font-family: "Libre Baskerville", serif; font-weight: 700;
    font-size: 28px; color: var(--gold);
  }
  .mark-rivet {
    position: absolute; left: 372px; top: 58px;
    display: flex; align-items: center; gap: 6px;
    font-family: "Libre Baskerville", serif; font-weight: 700;
    font-size: 22px; color: var(--gold);
  }
  .mark-rivet::before {
    content: ""; width: 16px; height: 16px; border-radius: 50%;
    background: var(--gold);
  }
  .coach-name {
    position: absolute; top: 112px; left: 0; width: 100%;
    text-align: center;
    font-family: "Libre Baskerville", serif; font-weight: 700;
    font-size: 29px; color: var(--gold);
    text-shadow: 0 0 6px var(--glow), 1px 1px 0 #000;
  }
  .coach-role {
    position: absolute; top: 153px; left: 0; width: 100%;
    text-align: center;
    font-family: "Libre Baskerville", serif; font-weight: 700;
    font-size: 17px; color: var(--gold);
    text-shadow: 0 0 5px var(--glow), 1px 1px 0 #000;
  }
  .contact-list { position: absolute; left: 96px; top: 184px; list-style: none; }
  .contact-item {
    display: flex; align-items: center; gap: 14px;
    height: 30px;
    font-family: "Libre Baskerville", serif; font-size: 13.5px;
    color: var(--gold-text);
    text-shadow: 0 0 4px var(--glow);
  }
  .contact-icon { width: 22px; height: 22px; flex: none; filter: drop-shadow(0 0 2px var(--glow)); }
</style>
</head>
<body>
<div class="canvas">

  <section class="card card--front" aria-label="Program side">
    <div class="net-decoration" role="img" aria-label="Faint basketball hoop and net in the background"></div>
    <h2 class="program-title">Basketball Training program</h2>

    <div class="offer offer--travel">
      <svg width="96" height="50" viewBox="0 0 100 56" aria-hidden="true">
        <path d="M6 10 Q8 4 16 4 H88 Q95 4 96 12 V44 H6 Z"/>
        <path d="M70 10 H90 V30 H70 Z"/>
        <path d="M14 14 H22 V22 H14 Z M26 14 H34 V22 H26 Z M38 14 H46 V22 H38 Z M50 14 H58 V22 H50 Z"/>
        <path d="M6 32 H96"/>
        <circle cx="22" cy="46" r="6"/><circle cx="78" cy="46" r="6"/>
      </svg>
      <div class="offer-label">Travel Club Program</div>
    </div>

    <div class="offer offer--camps">
      <svg width="60" height="44" viewBox="0 0 64 48" aria-hidden="true">
        <path d="M4 44 L30 6 L60 34 L44 44 Z"/>
        <path d="M30 6 L36 44"/>
        <path d="M4 44 L14 32 L22 44"/>
      </svg>
      <div class="offer-label">Camps</div>
    </div>

    <div class="offer offer--clinics">
      <svg width="60" height="48" viewBox="0 0 66 54" aria-hidden="true">
        <path d="M4 26 L33 4 L62 26"/>
        <path d="M46 14 V6 H54 V20"/>
        <path d="M10 22 V50 H56 V22"/>
        <path d="M28 20 H38 V28 H46 V38 H38 V46 H28 V38 H20 V28 H28 Z"/>
      </svg>
      <div class="offer-label">Clinics</div>
    </div>

    <div class="offer offer--private">
      <span class="player-figure" role="img" aria-label="Outline of a player dribbling a basketball"></span>
      <div class="offer-label">Private Training</div>
    </div>
  </section>

  <section class="card card--back" aria-label="Contact side">
    <div class="net-decoration" role="img" aria-label="Faint basketball hoop and net in the background"></div>
    <div class="mark-rb">RB</div>
    <div class="mark-rivet">RIVET</div>

    <h1 class="coach-name">Marlo Quintrell</h1>
    <p class="coach-role">Boys &amp; Girls Basketball Coach</p>

    <ul class="contact-list">
      <li class="contact-item">
        <svg class="contact-icon" viewBox="0 0 24 24" aria-hidden="true">
          <circle cx="12" cy="12" r="10" fill="none" stroke="var(--gold)" stroke-width="1.8"/>
          <path d="M2 12 H22 M12 2 Q5 12 12 22 M12 2 Q19 12 12 22" fill="none" stroke="var(--gold)" stroke-width="1.5"/>
        </svg>
        <span>Website: rivetbasketball.example</span>
      </li>
      <li class="contact-item">
        <svg class="contact-icon" viewBox="0 0 24 24" aria-hidden="true">
          <path d="M5 2 L9 2 L11 7 L8 9 Q10 14 15 16 L17 13 L22 15 L22 19 Q21 22 17 22 Q4 19 2 6 Q2 2 5 2 Z" fill="var(--gold)"/>
        </svg>
        <span>Main Phone: 555-317-4826</span>
      </li>
      <li class="contact-item">
        <svg class="contact-icon" viewBox="0 0 24 24" aria-hidden="true">
          <rect x="2" y="5" width="20" height="14" fill="none" stroke="var(--gold)" stroke-width="1.8"/>
          <path d="M2 5 L12 13 L22 5 M2 19 L9 11 M22 19 L15 11" fill="none" stroke="var(--gold)" stroke-width="1.5"/>
        </svg>
        <span>Email: rivet.basketball@mailbox.example</span>
      </li>
    </ul>
  </section>

</div>
</body>
</html>
```